Dr. Pelham Billboard Sign Design

Family Dental Practice looking for a billboard sign design. We have Attached a Image of Dr Pelham and Her horse she would like to incorporate. The size of the sign is 118" tall and 196" Wide. We hired a previous designer to work on this also but would like to see what other come up with before we decide on a final. Please use something similar for a animal shelter icon to go beside the Animal Shelter Discount statement. You can use the text from the postcard file attached. I know text adjustments will be needed, but more interested in a eye catching design. Themes: Fall/Winter/Mountains/Nature , colors: open but Dr P like purple. We are open to ideas and will answer any questions.
TEXT
Theme: Fall/Winter/Mountain
Image: Dr Pelham with Horse (Same from mailer design)
Text to Keep that needs to be bold and Priority
1. Dr. Rosalind Pelham Family Dentistry
417 Birch Lane Spruce Pine, NC 28704
828-555-3418 | RPelhamDDS@mailvexo.net
(FaceBook icon) RosalindPelhamDDS
2. ACCEPTING NEW PATIENTS
3. Affordable Dentistry for Your Whole Family
4. WE FILE YOUR INSURANCE CLAIMS
5. Discounts for Senior Citizens, Law Enforcement, First Responders, Military Personnel, State Employees and College Students
6. (Cool Animal Shelter Icon) WE OFFER A DISCOUNT TO PATIENTS WHO SUPPORT OUR LOCAL ANIMAL SHELTERS BY ADOPTING, DONATING OR VOLUNTEERING
7. Schedule Your Appointment TODAY!
Target Market(s)
Local Community to Bring in Patients to dental office
Industry/Entity Type
Dental
Look and feel

```html
<!DOCTYPE html>
<html lang="en">
<head>
<meta charset="utf-8">
<title>Dr. Pelham Billboard</title>
<link rel="stylesheet" href="https://fonts.googleapis.com/css2?family=Anton&family=Roboto:ital,wght@0,700;0,900;1,900&family=Roboto+Condensed:wght@700&display=swap">
<style>
  :root {
    --page: #e9e4ec;
    --forest-dark: #3a0a3a;
    --forest-mid: #a0237f;
    --forest-light: #d86fc4;
    --yellow: #ffff1a;
    --blue: #1a9cf0;
    --shadow: #2a1830;
    --ink: #111111;
    --white: #ffffff;
    --bullet: #8e2bd9;
  }
  html, body { margin: 0; width: 1200px; height: 1200px; overflow: hidden; background: var(--page); }
  .billboard-frame { position: absolute; left: 20px; top: 250px; width: 1160px; height: 700px; }
  .billboard {
    position: absolute; left: 0; top: 0; width: 1310px; height: 790px;
    transform: scale(0.8855); transform-origin: 0 0; overflow: hidden;
    font-family: "Roboto", sans-serif;
  }
  .scene-backdrop {
    position: absolute; inset: 0;
    background:
      radial-gradient(ellipse 40% 45% at 45% 35%, var(--forest-light), transparent 70%),
      linear-gradient(180deg, var(--forest-dark) 0%, var(--forest-mid) 45%, #7a1b63 70%, var(--forest-dark) 100%);
  }
  .practice-name {
    position: absolute; left: 55px; top: 26px; margin: 0;
    font: italic 900 74px/1 "Roboto", sans-serif; color: var(--yellow);
    text-shadow: 3px 3px 0 var(--ink); letter-spacing: -0.5px; white-space: nowrap;
  }
  .contact { position: absolute; left: 55px; font: 700 35px/1 "Roboto Condensed", sans-serif; color: var(--white); text-shadow: 2px 2px 0 var(--ink); white-space: nowrap; }
  .contact.address { top: 124px; }
  .contact.phone { top: 182px; }
  .cta { position: absolute; right: 568px; top: 238px; text-align: right; font-family: "Anton", sans-serif; line-height: 1; }
  .cta span { display: block; text-shadow: 3px 3px 0 var(--ink); }
  .cta .cta-schedule { font-size: 84px; color: var(--yellow); }
  .cta .cta-your { font-size: 58px; color: var(--yellow); margin-top: -2px; }
  .cta .cta-today { font-size: 76px; color: var(--white); }
  .feature {
    position: absolute; left: 783px; width: 540px; height: 78px;
    background: var(--blue); border-radius: 10px 0 0 10px; color: var(--white);
    box-shadow: -6px 7px 0 var(--shadow);
    display: flex; align-items: center; justify-content: center; text-align: center;
  }
  .feature.accepting { top: 142px; font: 40px/1 "Anton", sans-serif; }
  .feature.affordable { top: 237px; font: 700 29px/1.18 "Roboto", sans-serif; }
  .feature.insurance { top: 333px; font: 40px/1 "Anton", sans-serif; }
  .feature span { margin-right: 28px; }
  .discounts-tab {
    position: absolute; left: 1005px; top: 442px; width: 305px; height: 48px;
    background: var(--yellow); clip-path: polygon(14% 0, 100% 0, 100% 100%, 0 100%);
    font: 700 35px/48px "Roboto", sans-serif; color: var(--ink); text-align: right; padding-right: 20px; box-sizing: border-box;
  }
  .discounts-band {
    position: absolute; left: 395px; top: 490px; width: 915px; height: 110px;
    background: var(--white); clip-path: polygon(0 0, 100% 0, 100% 100%, 5% 100%);
  }
  .discount-list {
    position: absolute; left: 465px; top: 510px; margin: 0; padding: 0; list-style: none;
    display: grid; grid-template-columns: 283px 283px 260px; row-gap: 10px;
    font: 700 26px/1.1 "Roboto", sans-serif; color: var(--ink); white-space: nowrap;
  }
  .discount-list li::before {
    content: ""; display: inline-block; width: 9px; height: 9px; border-radius: 50%;
    border: 3px solid #c9a0ef; background: var(--bullet); margin-right: 6px; vertical-align: middle;
  }
  .doctor-photo {
    position: absolute; left: 0; top: 235px; width: 490px; height: 555px;
    background: linear-gradient(135deg, #4a2a20 0%, #6b4a3a 40%, #7c8a70 75%, #c9a8c4 100%);
    clip-path: polygon(12% 0, 48% 0, 70% 25%, 88% 55%, 100% 100%, 0 100%, 0 60%);
  }
  .social { position: absolute; left: 78px; top: 733px; display: flex; align-items: center; gap: 18px; color: var(--white); font: 700 30px/1 "Roboto Condensed", sans-serif; }
  .social-dot { width: 40px; height: 40px; border-radius: 50%; background: var(--white); }
  .shelter-icon {
    position: absolute; left: 518px; top: 618px; width: 140px; height: 152px;
    background: linear-gradient(160deg, #ffe21a 0%, #ff8a1a 55%, #2f8ee0 100%); border-radius: 10px;
  }
  .shelter-offer {
    position: absolute; left: 685px; top: 625px; width: 560px;
    font-family: "Anton", sans-serif; color: var(--white); text-shadow: 2px 2px 0 var(--ink);
    line-height: 1; white-space: nowrap;
  }
  .shelter-offer .headline { display: block; font-size: 54px; transform: scaleX(0.8); transform-origin: 0 50%; width: 125%; }
  .shelter-offer .detail { display: block; font-size: 32px; margin-top: 6px; }
  .highlight { color: var(--yellow); }
</style>
</head>
<body>
  <div class="billboard-frame">
    <section class="billboard">
      <div class="scene-backdrop" role="img" aria-label="Purple-tinted autumn forest with railroad tracks leading into the trees"></div>

      <h1 class="practice-name">Dr. Rosalind Pelham Family Dentistry</h1>
      <div class="contact address">417 Birch Lane Spruce Pine, NC 28704</div>
      <div class="contact phone">828-555-3418 | RPelhamDDS@mailvexo.net</div>

      <div class="cta">
        <span class="cta-schedule">Schedule</span>
        <span class="cta-your">Your Appointment</span>
        <span class="cta-today">TODAY!</span>
      </div>

      <div class="feature accepting"><span>ACCEPTING NEW PATIENTS</span></div>
      <div class="feature affordable"><span>AFFORDABLE DENTISTRY FOR<br>YOUR WHOLE FAMILY</span></div>
      <div class="feature insurance"><span>WE FILE YOUR INSURANCE CLAIMS</span></div>

      <div class="discounts-band"></div>
      <div class="discounts-tab">Discounts for</div>
      <ul class="discount-list">
        <li>Senior Citizens</li>
        <li>First Responders</li>
        <li>State Employees</li>
        <li>Law Enforcement</li>
        <li>Military Personnel</li>
        <li>College Students</li>
      </ul>

      <div class="doctor-photo" role="img" aria-label="Photo of Dr. Pelham standing with her brown horse"></div>

      <div class="social"><span class="social-dot"></span>RosalindPelhamDDS</div>

      <div class="shelter-icon" role="img" aria-label="Animal shelter icon: house with a dog and cat"></div>
      <div class="shelter-offer">
        <span class="headline">WE OFFER A <span class="highlight">DISCOUNT</span> TO PATIENTS</span>
        <span class="detail">WHO <span class="highlight">SUPPORT</span> OUR <span class="highlight">LOCAL ANIMAL SHELTERS</span></span>
        <span class="detail">BY ADOPTING, DONATING OR VOLUNTEERING</span>
      </div>
    </section>
  </div>
</body>
</html>
```